Australian IT Company New Logo Business Cards Required

We are a computer consultancy / MSP located in Brisbane Australia looking to have business cards designed with our new logo, we are looking for something professional that catches the eye.
I can provide the logo in other formats if required, let's see what you can create!

```html
<!DOCTYPE html>
<html lang="en">
<head>
<meta charset="utf-8">
<title>Norvale Business Cards</title>
<link rel="stylesheet" href="https://fonts.googleapis.com/css2?family=Open+Sans:wght@600&family=Poppins:wght@400;500;700&display=swap">
<style>
  :root {
    --backdrop: #1b1b1b;
    --card: #161616;
    --card-edge: #222222;
    --green: #7fc241;
    --grey: #8c8c8c;
    --white: #f2f2f2;
    --divider: #3a3a3a;
  }
  * { box-sizing: border-box; margin: 0; padding: 0; }
  html, body { width: 1200px; height: 1200px; overflow: hidden; }
  body {
    background: radial-gradient(circle at 70% 25%, #2a2a2a 0%, var(--backdrop) 60%);
    font-family: "Poppins", sans-serif;
    position: relative;
  }
  .card {
    position: absolute;
    left: 150px;
    width: 900px;
    height: 514px;
    border-radius: 26px;
    background: linear-gradient(135deg, var(--card-edge) 0%, var(--card) 55%, #121212 100%);
    box-shadow: 0 18px 40px rgba(0,0,0,0.55);
    overflow: hidden;
  }
  .card--front { top: 56px; }
  .card--back { top: 630px; }

  .signal-decor {
    position: absolute;
    left: -140px;
    bottom: -150px;
    width: 520px;
    height: 520px;
    border-radius: 50%;
    background: radial-gradient(circle, #0c0c0c 0%, #1a1a1a 45%, rgba(30,30,30,0) 70%);
  }
  .card--back .signal-decor { width: 440px; height: 440px; left: -170px; bottom: -170px; }

  .brand { position: absolute; }
  .brand__name {
    display: flex;
    align-items: center;
    gap: 14px;
    color: var(--green);
    font-family: "Poppins", sans-serif;
    font-weight: 700;
    font-size: 78px;
    line-height: 1;
    letter-spacing: 2px;
  }
  .brand__dot {
    width: 34px; height: 34px; border-radius: 50%;
    background: var(--green);
  }
  .brand__tagline {
    margin-top: 10px;
    color: var(--grey);
    font-family: "Open Sans", sans-serif;
    font-weight: 600;
    font-size: 19px;
    letter-spacing: 3.2px;
    text-transform: uppercase;
  }
  .card--front .brand { left: 240px; top: 170px; }
  .card--back .brand { left: 60px; top: 150px; }
  .card--back .brand__name { font-size: 64px; }
  .card--back .brand__tagline { font-size: 16px; letter-spacing: 2.6px; }

  .front__web {
    position: absolute;
    left: 0; right: 0; bottom: 46px;
    text-align: center;
    color: var(--grey);
    font-size: 19px;
    letter-spacing: 0.5px;
  }

  .back__divider {
    position: absolute;
    left: 500px; top: 60px;
    width: 2px; height: 390px;
    background: var(--divider);
  }
  .contact { position: absolute; left: 540px; top: 66px; width: 340px; }
  .contact__name {
    color: var(--green);
    font-weight: 700;
    font-size: 40px;
    line-height: 1;
    letter-spacing: 1px;
    text-transform: uppercase;
  }
  .contact__role {
    margin-top: 6px;
    color: var(--grey);
    font-weight: 500;
    font-size: 19px;
    letter-spacing: 3px;
    text-transform: uppercase;
  }
  .contact__list { list-style: none; margin-top: 24px; }
  .contact__item {
    display: flex;
    align-items: flex-start;
    gap: 14px;
    color: var(--white);
    font-size: 21px;
    line-height: 1.35;
  }
  .contact__item--address { margin-top: 14px; }
  .contact__icon { width: 18px; height: 18px; margin-top: 6px; flex: none; }
  .contact__icon path, .contact__icon circle, .contact__icon rect { fill: none; stroke: var(--green); stroke-width: 2; }
  .contact__icon .solid { fill: var(--green); stroke: none; }
</style>
</head>
<body>

<section class="card card--front">
  <div class="signal-decor" role="img" aria-label="Faint concentric signal rings in the corner"></div>
  <div class="brand">
    <div class="brand__name"><span class="brand__dot"></span>NORVALE</div>
    <div class="brand__tagline">IT Solutions for Small Business</div>
  </div>
  <div class="front__web">www.norvaleit.com</div>
</section>

<section class="card card--back">
  <div class="signal-decor" role="img" aria-label="Faint concentric signal rings in the corner"></div>
  <div class="brand">
    <div class="brand__name"><span class="brand__dot"></span>NORVALE</div>
    <div class="brand__tagline">IT Solutions for Small Business</div>
  </div>
  <div class="back__divider"></div>
  <div class="contact">
    <div class="contact__name">Daniel Reyes</div>
    <div class="contact__role">Managing Director</div>
    <ul class="contact__list">
      <li class="contact__item">
        <svg class="contact__icon" viewBox="0 0 18 18"><path class="solid" d="M3 1l4 1 1 4-2 1.5a10 10 0 0 0 4.5 4.5L12 10l4 1 1 4-2 2C8 17 1 10 1 3z"/></svg>
        <span>214-555-0182</span>
      </li>
      <li class="contact__item">
        <svg class="contact__icon" viewBox="0 0 18 18"><rect x="4" y="1" width="10" height="16" rx="2"/><circle class="solid" cx="9" cy="14" r="1"/></svg>
        <span>212-555-0147</span>
      </li>
      <li class="contact__item">
        <svg class="contact__icon" viewBox="0 0 18 18"><rect x="1" y="4" width="16" height="11" rx="1"/><path d="M1 4l8 6 8-6"/></svg>
        <span>daniel@norvaleit.com</span>
      </li>
      <li class="contact__item">
        <svg class="contact__icon" viewBox="0 0 18 18"><circle cx="9" cy="9" r="7.5"/><path d="M1.5 9h15M9 1.5c-4 4-4 11 0 15M9 1.5c4 4 4 11 0 15"/></svg>
        <span>www.norvaleit.com</span>
      </li>
      <li class="contact__item contact__item--address">
        <svg class="contact__icon" viewBox="0 0 18 18"><path class="solid" d="M9 1a6 6 0 0 0-6 6c0 4.5 6 10 6 10s6-5.5 6-10a6 6 0 0 0-6-6zm0 8.5a2.5 2.5 0 1 1 0-5 2.5 2.5 0 0 1 0 5z"/></svg>
        <span>42 Kelvin Road NW<br>Suite 210, Lakeview<br>MI 49012</span>
      </li>
    </ul>
  </div>
</section>

</body>
</html>
```